Automotive lighting company needs professional business card

Hello, we are an automotive lighting company and looking to have a professional business card designed for us. We have included some images which can be used on the card. Website is www.brightarcmotoring.com which has all of our details on it. Email is brightarcmotoring@kelvomail.com phone number is 1300 628 317 thank you guys!

Target Market(s)

Automotive industry

Contact Information for Business Card

Phone - 1300 628 317
Web - www.brightarcmotoring.com
Email - brightarcmotoring@kelvomail.com

Requirements
Must have
• Looking to have a dark theme. Elegant and professional. Needs to look and feel like a high quality card to represent high quality company.

```html
<!DOCTYPE html>
<html lang="en">
<head>
<meta charset="utf-8">
<title>Bright Arc Motoring – Business Card</title>
<link rel="stylesheet" href="https://fonts.googleapis.com/css2?family=Montserrat:wght@500;700;800&display=swap">
<style>
  :root {
    --page-bg: #2a2a2b;
    --card-bg: #111213;
    --card-edge: #1b1c1e;
    --brand-blue: #1a97d6;
    --text-light: #f2f4f6;
    --photo-dark: #141516;
    --photo-mid: #4a4d50;
  }
  * { margin: 0; padding: 0; box-sizing: border-box; }
  html, body {
    width: 1200px;
    height: 896px;
    overflow: hidden;
    background: var(--page-bg);
    font-family: "Montserrat", Arial, sans-serif;
  }
  .sheet {
    position: relative;
    width: 1200px;
    height: 896px;
  }
  .card {
    position: absolute;
    left: 300px;
    width: 600px;
    height: 360px;
    background: linear-gradient(160deg, var(--card-edge), var(--card-bg) 60%);
    box-shadow: 0 12px 30px rgba(0,0,0,0.55);
    overflow: hidden;
  }
  .card--front { top: 68px; }
  .card--back { top: 468px; }

  .wordmark {
    display: flex;
    align-items: center;
    gap: 12px;
    color: var(--brand-blue);
    font-weight: 800;
    text-transform: uppercase;
    letter-spacing: 0.04em;
    white-space: nowrap;
  }
  .wordmark__dot {
    width: 14px;
    height: 14px;
    border-radius: 50%;
    background: var(--brand-blue);
    flex: none;
  }
  .card--front .wordmark {
    position: absolute;
    left: 0; right: 0;
    top: 160px;
    justify-content: center;
    font-size: 36px;
  }
  .card--back .wordmark {
    position: absolute;
    left: 38px;
    top: 82px;
    font-size: 19px;
    letter-spacing: 0.02em;
    gap: 9px;
    z-index: 2;
  }
  .card--back .wordmark__dot { width: 10px; height: 10px; }

  .contact-list {
    position: absolute;
    left: 40px;
    top: 212px;
    list-style: none;
    color: var(--text-light);
    z-index: 2;
  }
  .contact-list li {
    display: flex;
    align-items: center;
    gap: 14px;
    height: 32px;
    font-size: 12.5px;
    font-weight: 500;
    white-space: nowrap;
  }
  .contact-list li.contact--phone {
    font-size: 20px;
    font-weight: 700;
    height: 38px;
  }
  .contact-list svg {
    width: 17px;
    height: 17px;
    flex: none;
  }
  .product-photo {
    position: absolute;
    left: 356px;
    top: 50px;
    width: 244px;
    height: 310px;
    background:
      radial-gradient(ellipse at 50% 55%, var(--photo-mid), transparent 65%),
      linear-gradient(180deg, var(--card-bg), var(--photo-dark));
  }
</style>
</head>
<body>
<main class="sheet">
  <section class="card card--front" aria-label="Business card front">
    <div class="wordmark">
      <span class="wordmark__dot"></span>
      <span class="wordmark__name">Bright Arc Motoring</span>
    </div>
  </section>

  <section class="card card--back" aria-label="Business card back">
    <div class="product-photo" role="img" aria-label="Photo of two silver LED headlight bulbs with braided heat-sink tails standing on a reflective black surface"></div>

    <div class="wordmark">
      <span class="wordmark__dot"></span>
      <span class="wordmark__name">Bright Arc Motoring</span>
    </div>

    <ul class="contact-list">
      <li class="contact--phone">
        <svg viewBox="0 0 24 24" fill="none" stroke="var(--brand-blue)" stroke-width="1.6" stroke-linejoin="round">
          <path d="M5 3h4l2 5-2.5 1.5a11 11 0 0 0 6 6L16 13l5 2v4a2 2 0 0 1-2 2A16 16 0 0 1 3 5a2 2 0 0 1 2-2z"/>
        </svg>
        <span>1300 628 317</span>
      </li>
      <li>
        <svg viewBox="0 0 24 24">
          <rect x="2" y="5" width="20" height="14" rx="1.5" fill="var(--brand-blue)"/>
          <path d="M2.5 6l9.5 7 9.5-7" fill="none" stroke="var(--card-bg)" stroke-width="1.6"/>
        </svg>
        <span>brightarcmotoring@kelvomail.com</span>
      </li>
      <li>
        <svg viewBox="0 0 24 24" fill="none" stroke="var(--brand-blue)" stroke-width="1.8">
          <circle cx="12" cy="12" r="9.5"/>
          <ellipse cx="12" cy="12" rx="4.2" ry="9.5"/>
          <path d="M2.5 12h19M4 7h16M4 17h16"/>
        </svg>
        <span>www.brightarcmotoring.com</span>
      </li>
    </ul>
  </section>
</main>
</body>
</html>
```